New furniture company needs a cool, fresh Website - think lounjo.com, velmora.com

Tuftwell.com: We are launching a home (Storvane) furniture business, aimed at the young, discerning mid-market consumer. The aim is to compete with many furniture e-tailers, as well as more established retail brands.
We want the website to capture the hearts, minds and wallets of the target audience, placing Tuftwell.com firmly into the market place. Please look to Velmora.com for look and feel inspiration. We will be selling approx 15 products to start. I suggest using Storvane with the following theme please: – Hearth & Meadow – Radiance – Belmont. Please see the logo below. The website needs to have a sophisticated feel for affordable aspirational furniture. Soft colours and homely text - please go with look and feel of Velmora.com. Please see a below file containing image of some sofas, chairs and footstools that will be for sale.
Many thanks

Target Market(s)

mid-market, young families looking for cool, affordable, easy to buy furniture

Industry/Entity Type

Furniture

Coding

Coded - Design and coding required

Number of Pages Required

5+ page

Font styles to use
Sans Serif

Colors
86cae7
cee9f5
3277b5
eaf2ce
fdf9ce
fff3d1
0255a3
e8e8e8
cbcbcb

Requirements
Must have
• Storvane
• http://www.velmora.com/hartwick-leather-large-sofa.html - great example of what we need it to look like
• logo as shown
• homepage
• products menu - sofas, seating, footstools, antique
• images of all products (examples provided) with ability to click on various fabric swatch samples and see the sofa in different fabrics and colours (check out lounjo.com)
• facility for social media
• facility to buy online
• "add to wishlist"
• "add to basket"
Nice to have
• I want it to have a light and airy feel, nothing too heavy or corporate. Needs to be very easily navigated and a simple approach
Should not have
• Dark, heavy colours

```html
<!DOCTYPE html>
<html lang="en">
<head>
<meta charset="utf-8">
<title>Tuftwell — Home</title>
<link href="https://fonts.googleapis.com/css2?family=Raleway:wght@300;400&family=Lato:wght@400;700&display=swap" rel="stylesheet">
<style>
:root{
  --ink:#333;
  --muted:#777;
  --line:#d6d6d6;
  --brand-grey:#9a9aa2;
  --deep-blue:#0255a3;
  --sage:#e8efcb;
  --stone:#e8e8e8;
  --white:#fff;
}
*{box-sizing:border-box;margin:0;padding:0}
html,body{width:783px;height:1200px;overflow:hidden;background:var(--white)}
body{position:relative;font-family:"Lato",sans-serif;color:var(--ink)}
.abs{position:absolute}
.heading{font-family:"Raleway",sans-serif;font-weight:300;text-transform:uppercase;letter-spacing:.5px;line-height:1}
.kicker{font-family:"Lato",sans-serif;font-size:9px;text-transform:uppercase;letter-spacing:.3px}
.btn{position:absolute;border:1px solid currentColor;font-size:7.5px;display:flex;align-items:center;justify-content:center;letter-spacing:.3px}

/* header */
.social{top:8px;left:26px;display:flex;gap:9px}
.social span{width:6px;height:6px;border-radius:50%;background:#888;display:block}
.account{top:9px;right:30px;font-size:6px;letter-spacing:.3px;display:flex;gap:13px;text-transform:uppercase}
.brand{top:38px;left:0;width:783px;text-align:center;font-family:"Raleway",sans-serif;font-weight:400;font-size:13px;letter-spacing:4px;color:#8a8a8a}
.brand-dot{top:14px;left:383px;width:17px;height:17px;border:1.5px solid #999;border-radius:50%}
.tools{top:60px;left:708px;display:flex;gap:10px}
.rule{top:76px;left:18px;width:747px;border-top:1px solid var(--line)}
.nav{top:86px;left:0;width:783px;display:flex;justify-content:center;gap:22px;font-size:6.4px;text-transform:uppercase;letter-spacing:.2px}

/* hero */
.hero{top:106px;left:17px;width:749px;height:286px;background:linear-gradient(180deg,#c9cfcc 0%,#d9dcd8 45%,#b9bbb8 75%,#8f8c86 100%)}
.hero-panel{top:246px;left:510px;width:232px;height:104px;background:rgba(235,238,240,.72);text-align:right;padding:18px 22px 0 0;font-family:"Raleway",sans-serif;font-weight:300;font-size:35px;line-height:38px;color:#222}

/* tiles */
.tile{position:absolute;overflow:hidden}
.wallet{top:394px;left:17px;width:438px;height:211px;background:linear-gradient(180deg,#6a6d7c 0%,#5e6170 55%,#3a3b42 100%);color:var(--white)}
.antique{top:394px;left:457px;width:309px;height:211px;background:linear-gradient(160deg,#dfe4ec 0%,#c9d2df 40%,#eceff2 70%,#a9abaa 100%);color:#222}
.frame{position:absolute;border:1px solid rgba(255,255,255,.7)}
.delivery{top:607px;left:17px;width:248px;height:113px;background:var(--deep-blue);color:var(--white);text-align:center}
.decors{top:722px;left:17px;width:248px;height:113px;background:linear-gradient(100deg,#e9e9de 0%,#f3f3ee 50%,#7fb0cf 80%,#e4eaef 100%);color:#222}
.sitters{top:607px;left:268px;width:248px;height:228px;background:linear-gradient(180deg,#efefef 0%,#e5e6e8 40%,#6f8596 70%,#8a94a0 100%);color:#222}
.about{top:607px;left:519px;width:247px;height:228px;background:var(--sage);color:#222;text-align:center}
.find{top:838px;left:17px;width:248px;height:196px;background:var(--stone)}
.news{top:838px;left:268px;width:498px;height:196px;background:linear-gradient(180deg,#6c7387 0%,#5e6578 55%,#3e4048 80%,#707563 100%);color:var(--white);text-align:center}

.contact{display:flex;align-items:flex-start;gap:14px;font-size:9px;line-height:11px;position:absolute;left:28px}
.input{position:absolute;top:61px;left:121px;width:193px;height:20px;border:1px solid rgba(255,255,255,.8);font-size:6.5px;text-align:left;padding:6px 10px}
.submit{position:absolute;top:61px;left:319px;width:59px;height:20px;background:var(--white);color:#222;font-size:9px;display:flex;align-items:center;justify-content:center;letter-spacing:.4px}

/* footer */
.footer{top:1037px;left:17px;width:749px;height:163px;background:var(--brand-grey);color:var(--white)}
.footer .brand{top:68px;width:749px;color:#eee;font-size:13px}
.footer-dot{top:31px;left:366px;width:17px;height:17px;border:1.5px solid #eee;border-radius:50%}
.footer-rule{top:106px;left:286px;width:177px;border-top:1px solid rgba(255,255,255,.7)}
.copy{top:135px;left:10px;font-size:6.5px}
.fsocial{top:136px;left:343px;display:flex;gap:11px}
.fsocial span{width:6px;height:6px;border-radius:50%;background:#fff;display:block}
.flinks{top:136px;left:531px;display:flex;gap:14px;font-size:6.5px}
.top-btn{top:124px;left:716px;width:20px;height:20px;border:1px solid #fff;border-radius:50%}
</style>
</head>
<body>

<header>
  <div class="abs social"><span></span><span></span><span></span><span></span></div>
  <div class="abs brand-dot"></div>
  <div class="abs brand">TUFTWELL</div>
  <div class="abs account"><span>Login / Register</span><span>Wishlist</span></div>
  <div class="abs tools">
    <svg width="13" height="13" viewBox="0 0 13 13" fill="none" stroke="#777" stroke-width="1"><circle cx="5.5" cy="5.5" r="4.5"/><line x1="9" y1="9" x2="12.5" y2="12.5"/></svg>
    <svg width="22" height="14" viewBox="0 0 22 14" fill="none" stroke="#777" stroke-width="1"><path d="M0 1h3l2 8h9l2-6H4"/><circle cx="6" cy="12" r="1.2"/><circle cx="13" cy="12" r="1.2"/><circle cx="18" cy="10" r="3.5" fill="#1f6fb8" stroke="none"/><text x="18" y="12" font-size="5" fill="#fff" text-anchor="middle" stroke="none" font-family="Lato,sans-serif">0</text></svg>
  </div>
  <div class="abs rule"></div>
  <nav class="abs nav"><span>Shop Collections</span><span>Gallery</span><span>Designers</span><span style="margin-left:12px">Services</span><span>About Us</span><span>Showrooms</span></nav>
</header>

<section class="abs hero" role="img" aria-label="Bright living room with a grey corner sofa, light wood coffee table and white vases"></section>
<div class="abs hero-panel">Launching<br>Offer</div>

<section class="tile wallet" role="img" aria-label="Cream sofa with blue and rust cushions against a grey wall">
  <div class="abs kicker" style="top:29px;right:30px;font-size:9px">Wallet Friendly</div>
  <div class="abs heading" style="top:40px;right:30px;font-size:19px">Collection</div>
  <div class="btn" style="top:64px;left:322px;width:85px;height:23px">View products</div>
</section>

<section class="tile antique" role="img" aria-label="Ceramic jugs, bowls and a blue glass vase on a table">
  <div class="frame" style="top:7px;left:6px;width:296px;height:197px"></div>
  <div class="abs kicker" style="top:70px;right:27px">Sofisticated</div>
  <div class="abs heading" style="top:80px;right:27px;font-size:19px">Antiques</div>
  <div class="btn" style="top:106px;left:203px;width:85px;height:23px">View products</div>
</section>

<section class="tile delivery">
  <div class="frame" style="top:7px;left:7px;width:234px;height:100px;border-color:rgba(255,255,255,.5)"></div>
  <div class="abs" style="top:30px;width:248px;font-size:8.5px">On orders over $150</div>
  <div class="abs heading" style="top:43px;width:248px;font-size:15px">Free Delivery Option</div>
  <div class="abs" style="top:66px;left:30px;width:188px;font-size:6px;line-height:8px;opacity:.85">Lorem ipsum dolor sit amet, consectetuer adipiscing elit, sed diam nonummy</div>
</section>

<section class="tile decors" role="img" aria-label="Tall blue glass vases in front of white and yellow cushions">
  <div class="abs kicker" style="top:30px;left:21px">Impressive</div>
  <div class="abs heading" style="top:40px;left:20px;font-size:19px">Decors</div>
  <div class="btn" style="top:71px;left:21px;width:85px;height:23px">View products</div>
</section>

<section class="tile sitters" role="img" aria-label="Blue upholstered footstool in front of a fireplace on a patterned rug">
  <div class="frame" style="top:9px;left:8px;width:232px;height:211px;border-color:rgba(180,180,180,.6)"></div>
  <div class="abs kicker" style="top:27px;left:22px">Wide renge of</div>
  <div class="abs heading" style="top:37px;left:21px;font-size:19px">Sitters</div>
  <div class="btn" style="top:64px;left:22px;width:85px;height:23px">View products</div>
</section>

<section class="tile about">
  <div class="frame" style="top:7px;left:7px;width:233px;height:214px;border-color:#cfd6b4"></div>
  <div class="abs" style="top:39px;left:53px;width:141px;border-top:1px solid #555"></div>
  <div class="abs heading" style="top:49px;width:247px;font-size:19px;line-height:22px">About<br>Tuftwell</div>
  <div class="abs" style="top:117px;left:23px;width:201px;font-size:6.4px;line-height:9.6px;color:#555">Lorem ipsum dolor sit amet, consectetuer adipiscing elit, sed diam nonummy nibh euismod tincidunt ut laoreet dolore magna aliquam erat volutpat. Ut wisi enim ad minim veniam, quis nostrud exerci tation ullamcorper suscipit lobortis nisl ut aliquip ex ea commodo consequat duis autem</div>
  <div class="btn" style="top:179px;left:81px;width:85px;height:23px">Read more</div>
</section>

<section class="tile find">
  <div class="frame" style="top:7px;left:7px;width:234px;height:182px;border-color:#cbcbcb"></div>
  <div class="abs heading" style="top:37px;left:28px;font-size:19px">Find Us</div>
  <div class="contact" style="top:77px">
    <svg width="12" height="16" viewBox="0 0 12 16" fill="none" stroke="#555"><path d="M6 15S1 9 1 6a5 5 0 0 1 10 0c0 3-5 9-5 9z"/><circle cx="6" cy="6" r="2"/></svg>
    <span>14 Larkspur Lane<br>Fenwick Hill, CT 06190</span>
  </div>
  <div class="contact" style="top:113px">
    <svg width="14" height="14" viewBox="0 0 14 14" fill="none" stroke="#555"><path d="M2 1l3 0 1 3-2 1.5c1 2 2.5 3.5 4.5 4.5L10 8l3 1v3c-6 1-12-5-11-11z"/></svg>
    <span style="margin-top:2px">+00 0000 0000 000</span>
  </div>
  <div class="contact" style="top:146px">
    <svg width="15" height="12" viewBox="0 0 15 12" fill="none" stroke="#555"><rect x="0.5" y="0.5" width="14" height="11"/><path d="M.5 .5l7 6 7-6"/></svg>
    <span style="margin-top:1px">info@tuftwell.com</span>
  </div>
</section>

<section class="tile news" role="img" aria-label="White sectional sofa with green cushions under a grey pendant lamp">
  <div class="abs heading" style="top:23px;width:498px;font-size:17px">Newsletter</div>
  <div class="abs" style="top:47px;width:498px;font-size:7.5px">Subscribe to our newsletter and know about our latest deals and offers.</div>
  <div class="input">Enter name...</div>
  <div class="submit">SUBMIT</div>
</section>

<footer class="abs footer">
  <div class="abs footer-dot"></div>
  <div class="abs brand">TUFTWELL</div>
  <div class="abs footer-rule"></div>
  <div class="abs copy">Copyright © Tuftwell 2017</div>
  <div class="abs fsocial"><span></span><span></span><span></span><span></span></div>
  <div class="abs flinks"><span>Products</span><span>Contact Us</span><span>Site Map</span><span>About Us</span></div>
  <svg class="abs top-btn" viewBox="0 0 20 20" fill="none" stroke="#fff"><path d="M6 12l4-4 4 4"/></svg>
</footer>

</body>
</html>
```